Business card

Looking for modern clean business card off logo below. Very important to be clean and professional but want fun as well

Industry/Entity Type

Business

```html
<!DOCTYPE html>
<html lang="en">
<head>
<meta charset="utf-8">
<title>Keystone Homes — Business Card</title>
<link rel="stylesheet" href="https://fonts.googleapis.com/css2?family=Bebas+Neue&family=Questrial&family=Tinos&display=swap">
<style>
  :root {
    --sky: #cdf8fb;
    --card: #f2f3ef;
    --slate: #4f5a5f;
    --teal: #5de0dc;
    --ink: #2b2b2b;
    --pink: #f0266f;
    --orange: #f57f1f;
    --charcoal: #2a2a2a;
    --mint: #7fe8cf;
  }
  * { margin: 0; padding: 0; box-sizing: border-box; }
  html, body { width: 900px; height: 1200px; overflow: hidden; background: var(--sky); }
  .canvas { position: relative; width: 900px; height: 1200px; background: var(--sky); }

  .card { position: absolute; left: 0; width: 900px; background: var(--card); }
  .card--front { top: 70px; height: 500px; }
  .card--back { top: 590px; height: 498px; }

  .brand-dot {
    position: absolute; left: 130px; top: 162px;
    width: 200px; height: 200px; border-radius: 50%;
    background: var(--teal);
  }
  .brand-name {
    position: absolute; left: 372px; top: 196px;
    font-family: "Bebas Neue", sans-serif;
    font-size: 92px; line-height: 1; letter-spacing: 1px;
    color: var(--slate);
  }
  .brand-tagline {
    position: absolute; left: 386px; top: 276px;
    font-family: "Questrial", sans-serif;
    font-size: 22px; color: var(--slate);
  }

  .about {
    position: absolute; left: 0; width: 900px; top: 104px;
    text-align: center;
    font-family: "Tinos", serif;
    font-size: 28px; line-height: 29px; color: var(--ink);
  }

  .contact { position: absolute; display: flex; align-items: center; }
  .contact__icon { width: 75px; height: 75px; flex: none; }
  .contact__text { font-family: "Tinos", serif; color: var(--ink); }

  .contact--address { left: 118px; top: 263px; }
  .contact--address .contact__text { margin-left: 30px; font-size: 25px; }
  .contact--phone { left: 118px; top: 354px; }
  .contact--phone .contact__text { margin-left: 28px; font-size: 25px; }
  .contact--web { left: 526px; top: 262px; }
  .contact--web .contact__text { margin-left: 26px; font-size: 24px; margin-top: -14px; }
  .contact--mail { left: 527px; top: 354px; }
  .contact--mail .contact__text { margin-left: 66px; font-size: 29px; }
</style>
</head>
<body>
<main class="canvas">
  <section class="card card--front">
    <div class="brand-dot"></div>
    <div class="brand-name">Keystone Homes</div>
    <div class="brand-tagline">Property Management and Real Estate</div>
  </section>

  <section class="card card--back">
    <p class="about">A few Words about your company<br>A few Words about your company<br>A few Words about your company</p>

    <div class="contact contact--address">
      <svg class="contact__icon" viewBox="0 0 75 75" aria-hidden="true">
        <circle cx="37.5" cy="37.5" r="37.5" fill="var(--pink)"/>
        <path d="M19 38 L37.5 21 L56 38" fill="none" stroke="#fff" stroke-width="4" stroke-linejoin="round" stroke-linecap="round"/>
        <path d="M25 36 V54 H33 V44 H42 V54 H50 V36 L37.5 25 Z" fill="#fff"/>
      </svg>
      <span class="contact__text">Your Address here</span>
    </div>

    <div class="contact contact--phone">
      <svg class="contact__icon" viewBox="0 0 75 75" aria-hidden="true">
        <circle cx="37.5" cy="37.5" r="37.5" fill="var(--orange)"/>
        <path d="M26 20 C23 21 20 24 21 29 C23 40 34 51 45 54 C50 55 53 52 54 49 L47 43 L42 46 C37 44 31 38 29 33 L32 28 Z" fill="#fff"/>
      </svg>
      <span class="contact__text">Contact No.’s</span>
    </div>

    <div class="contact contact--web">
      <svg class="contact__icon" viewBox="0 0 75 75" aria-hidden="true">
        <circle cx="37.5" cy="37.5" r="37.5" fill="var(--charcoal)"/>
        <g fill="none" stroke="#fff" stroke-width="2.5">
          <circle cx="37.5" cy="37.5" r="17"/>
          <ellipse cx="37.5" cy="37.5" rx="7.5" ry="17"/>
          <line x1="37.5" y1="20.5" x2="37.5" y2="54.5"/>
          <line x1="20.5" y1="37.5" x2="54.5" y2="37.5"/>
          <line x1="23" y1="29" x2="52" y2="29"/>
          <line x1="23" y1="46" x2="52" y2="46"/>
        </g>
      </svg>
      <span class="contact__text">www.website.com</span>
    </div>

    <div class="contact contact--mail">
      <svg class="contact__icon" viewBox="0 0 75 75" aria-hidden="true">
        <circle cx="37.5" cy="37.5" r="37.5" fill="var(--mint)"/>
        <g fill="none" stroke="#fff" stroke-width="2.5" stroke-linejoin="round">
          <rect x="18" y="25" width="39" height="26"/>
          <path d="M18 25 L37.5 40 L57 25"/>
          <path d="M18 51 L32 36 M57 51 L43 36"/>
        </g>
      </svg>
      <span class="contact__text">@mail.com</span>
    </div>
  </section>
</main>
</body>
</html>
```